Design my dad a new business card because his current one sucks!

I need a business card designed for my fathers home maintenance business. His customers are individuals (single moms, old people etc.) as well as the occasional business. As such it needs to be accessible to both target audiences.

The front of the card should be dark grey on yellow with the logo and contain the following information:
- Warren Dobrinski
- 0487 362 914
- info@harbourlinehandyworks.com.au
- 0487 362 914

- ABN: 87 214 630 592
- 'Fully Insured'

The reverse should be yellow on dark grey and will have the web address:
- harbourlinehandyworks.com.au

And a few key services he offers:
GENERAL REPAIRS
PAINTING/TILING/
PAVING &CONCRETING
PRESSURE WASHING
ON-SITE WELDING
DECKING ADDITIONS & REPAIRS
FENCING
FULL BOND CLEANING

This will be first time the logo has been printed so you will need to come up with the best CMYK approximation of the RGB colours to make sure it is a close as possible.

```html
<!DOCTYPE html>
<html lang="en">
<head>
<meta charset="utf-8">
<title>Harbourline Handyworks – Business Card</title>
<link rel="stylesheet" href="https://fonts.googleapis.com/css2?family=Open+Sans:wght@400;700&display=swap">
<style>
  :root {
    --yellow-core: #ffec00;
    --yellow-mid: #fdd900;
    --yellow-edge: #f6c200;
    --ink: #3c3c3c;
    --mark-ink: #231f20;
  }
  html, body {
    margin: 0;
    padding: 0;
    overflow: hidden;
    background: #ffffff;
  }
  .card {
    position: relative;
    width: 1200px;
    height: 686px;
    overflow: hidden;
    background: radial-gradient(ellipse 70% 75% at 58% 36%, var(--yellow-core) 0%, var(--yellow-mid) 55%, var(--yellow-edge) 100%);
    font-family: "Open Sans", Arial, sans-serif;
    color: var(--ink);
  }
  .brand-name {
    position: absolute;
    left: 270px;
    width: 643px;
    top: 138px;
    margin: 0;
    text-align: right;
    font-size: 104px;
    font-weight: 700;
    line-height: 108px;
    letter-spacing: -1px;
    color: var(--mark-ink);
  }
  .brand-name span {
    display: block;
    white-space: nowrap;
  }
  .insured {
    position: absolute;
    right: 287px;
    top: 367px;
    margin: 0;
    font-size: 27px;
    font-weight: 400;
    line-height: 1.2;
  }
  .owner-name {
    position: absolute;
    left: 32px;
    top: 414px;
    margin: 0;
    font-size: 44px;
    font-weight: 700;
    line-height: 1.2;
  }
  .contact {
    position: absolute;
    left: 180px;
    display: flex;
    align-items: center;
    margin: 0;
    font-size: 36px;
    font-weight: 400;
    line-height: 1;
  }
  .contact svg {
    width: 64px;
    height: 52px;
    margin-right: 58px;
    flex: none;
  }
  .contact--phone { top: 522px; }
  .contact--email { top: 594px; }
  .abn {
    position: absolute;
    right: 18px;
    bottom: 10px;
    margin: 0;
    font-size: 26px;
    font-weight: 400;
    line-height: 1.2;
  }
</style>
</head>
<body>
  <main class="card">
    <h1 class="brand-name"><span>Harbourline</span><span>Handyworks</span></h1>
    <p class="insured">Fully Insured</p>

    <p class="owner-name">Warren Dobrinski</p>

    <p class="contact contact--phone">
      <svg viewBox="0 0 64 52" aria-hidden="true" fill="none" stroke="var(--ink)" stroke-width="3" stroke-linejoin="round">
        <path d="M4 16 C4 6 18 3 32 3 C46 3 60 6 60 16 L60 20 L48 20 L48 13 L16 13 L16 20 L4 20 Z"/>
        <path d="M18 18 L12 48 L52 48 L46 18"/>
        <circle cx="32" cy="32" r="8"/>
        <circle cx="32" cy="32" r="2.5" fill="var(--ink)"/>
      </svg>
      <span>0487 362 914</span>
    </p>

    <p class="contact contact--email">
      <svg viewBox="0 0 64 52" aria-hidden="true" fill="none" stroke="var(--ink)" stroke-width="3" stroke-linejoin="round">
        <rect x="3" y="10" width="58" height="32" rx="2"/>
        <path d="M3 12 L32 32 L61 12"/>
        <path d="M3 42 L24 26 M61 42 L40 26"/>
      </svg>
      <span>info@harbourlinehandyworks.com.au</span>
    </p>

    <p class="abn">ABN: 87 214 630 592</p>
  </main>
</body>
</html>
```